Boat business cards

I'm looking for business cards with the two logos I've attached. I don't have an specific idea in mind and open to anything. All the usual info will be on the card. Name, position in company, nr, email, address, ect. The company rents out these two boats for charters and fishing.

```html
<!DOCTYPE html>
<html lang="en">
<head>
<meta charset="utf-8">
<title>Charter Business Card</title>
<link href="https://fonts.googleapis.com/css2?family=Open+Sans:wght@400;600;700&display=swap" rel="stylesheet">
<style>
  :root {
    --page: #e4e6e7;
    --card: #ffffff;
    --ink: #1c1c1c;
    --accent-blue: #6f9acb;
    --accent-brown: #8a6a45;
    --hull-brown: #a88a66;
    --hull-blue: #8fa9cf;
  }
  * { margin: 0; padding: 0; box-sizing: border-box; }
  html, body { width: 1200px; height: 928px; overflow: hidden; }
  body {
    background: var(--page);
    font-family: "Open Sans", sans-serif;
    color: var(--ink);
    position: relative;
  }
  .card {
    position: absolute;
    left: 262px;
    width: 676px;
    height: 386px;
    background: var(--card);
    border-radius: 16px;
  }
  .card--front { top: 56px; }
  .card--back { top: 486px; }

  .brand { position: absolute; text-align: center; }
  .brand__art {
    border-radius: 8px;
  }
  .brand__name {
    font-size: 24px;
    font-weight: 700;
    color: var(--ink);
    margin-top: 10px;
    letter-spacing: 1px;
  }
  .brand--yacht { left: 48px; top: 168px; width: 270px; }
  .brand--yacht .brand__art {
    height: 70px;
    background: linear-gradient(180deg, #f1f1f1 0%, #d9d9d9 40%, var(--hull-brown) 70%, #c9d7ea 100%);
  }
  .brand--sportfisher { left: 360px; top: 116px; width: 262px; }
  .brand--sportfisher .brand__art {
    height: 110px;
    background: linear-gradient(180deg, #f4f4f4 0%, #d6d8dc 50%, var(--hull-blue) 80%, #9aa3ad 100%);
  }

  .person {
    position: absolute;
    right: 366px;
    top: 160px;
    text-align: right;
  }
  .person__name {
    font-size: 27px;
    font-weight: 700;
    color: var(--accent-blue);
    line-height: 1.1;
  }
  .person__role {
    font-size: 15px;
    margin-top: 10px;
  }

  .contact {
    position: absolute;
    left: 362px;
    top: 152px;
    list-style: none;
  }
  .contact__item {
    display: flex;
    align-items: center;
    gap: 8px;
    font-size: 16px;
    height: 29px;
  }
  .contact__item--phone { letter-spacing: 2px; }
  .contact__icon { width: 17px; height: 17px; fill: var(--accent-brown); flex: none; }

  .address {
    position: absolute;
    left: 0; right: 0;
    top: 312px;
    text-align: center;
    font-size: 16px;
    letter-spacing: 0.3px;
  }
  .address__pin { display: block; margin: 0 auto 6px; width: 18px; height: 24px; fill: var(--accent-brown); }
</style>
</head>
<body>
  <section class="card card--front">
    <div class="brand brand--yacht">
      <div class="brand__art" role="img" aria-label="Illustration of a luxury motor yacht with a brown hull"></div>
      <div class="brand__name">HARBOR LANTERN</div>
    </div>
    <div class="brand brand--sportfisher">
      <div class="brand__art" role="img" aria-label="Illustration of a blue sport fishing boat with tower and outriggers"></div>
      <div class="brand__name">SEA BREEZE</div>
    </div>
  </section>

  <section class="card card--back">
    <div class="person">
      <div class="person__name">Marla Keaton</div>
      <div class="person__role">Director</div>
    </div>
    <ul class="contact">
      <li class="contact__item contact__item--phone">
        <svg class="contact__icon" viewBox="0 0 24 24"><path d="M6.6 10.8a15.1 15.1 0 0 0 6.6 6.6l2.2-2.2a1 1 0 0 1 1-.25 11.4 11.4 0 0 0 3.6.57 1 1 0 0 1 1 1V20a1 1 0 0 1-1 1A17 17 0 0 1 3 4a1 1 0 0 1 1-1h3.5a1 1 0 0 1 1 1c0 1.25.2 2.45.57 3.57a1 1 0 0 1-.25 1z"/></svg>
        555-014-2286
      </li>
      <li class="contact__item">
        <svg class="contact__icon" viewBox="0 0 24 24"><path d="M2 5h20v14H2z M2 5l10 7 10-7" /><path d="M3 6l9 6.3L21 6v1.4l-9 6.3-9-6.3z" fill="#fff"/></svg>
        marla@tidewaycharters.com
      </li>
      <li class="contact__item">
        <svg class="contact__icon" viewBox="0 0 24 24"><circle cx="12" cy="12" r="10"/><path d="M7 7c2 0 3 1 3 3s-2 2-2 4 2 2 2 4M15 5c-1 2 0 3 2 4s2 3 1 5" stroke="#fff" stroke-width="1.6" fill="none"/></svg>
        www.tidewaycharters.com
      </li>
    </ul>
    <div class="address">
      <svg class="address__pin" viewBox="0 0 18 24"><path d="M9 0a9 9 0 0 0-9 9c0 6.5 9 15 9 15s9-8.5 9-15a9 9 0 0 0-9-9zm0 12.5A3.5 3.5 0 1 1 9 5.5a3.5 3.5 0 0 1 0 7z"/></svg>
      4120 Harbor Point Rd, Suite 118, Bayview, OH 45000
    </div>
  </section>
</body>
</html>
```